Church needs a very simple, quality infographic to communicate their process

I just updated the brief with two images of a design idea that I like which I would like to see worked into my brief.
Considering those new pics, I would remove the words "up, in, out" and put in "god, the church, the world". I would put "connect in every direction" somewhere in the design. I would try to represent how we want to connect each person in each of those directions. Lastly, I would try to show a connection between those three things and a person.
Design Needs:A simple infographic that clearly communicates our discipleship pathway without requiring additional explanation. Discipleship Process:• In order for someone in our church to be completely discipled they must “connect in every direction”. They must connect …o Up to God o In to the Churcho Out to the WorldTone and Manner:• The main objective is that someone new to the church could look at the infographic and understand that our church wants to help them connect up to God, in to the church, and out to the world and that’s what they are supposed to do. • Intuitive and obvious to understand.• Simple and clear.• Same color as our logo and values (if possible). • Our church’s mission is “Connecting Young Families to Christ” so our focus is to reach out to families while not being exclusive to others. • Our church’s core values are: Equipping, Serving, Belonging, Missional Living, Spirit-living• Our target audience is families with school-aged kids. • Our website is www.lakerowchapel.ca • Our church is an evangelical Christian church about 50 years old, located in Mississauga, Canada, and recently went through a church relaunch where we came up with a new mission, vision, and values, and now our discipleship pathway. • I would like the infographic to have a real quality to it which reflects the amount of effort and care we put into crafting our discipleship pathway and how important it is going forward. Further Requests:• I intend to place this infographic on a wall in the main auditorium (5 feet x 5 feet) and be able to place it on documents, posters, website, etc.• Needs to be quality enough to scale way up and resize. • Will need the graphic completed by May 14th.Please contact Lead Pastor, Darren Holloway darren@lakerowchapel.ca

```html
<!DOCTYPE html>
<html lang="en">
<head>
<meta charset="utf-8">
<title>Connect in Every Direction – Lakerow Family Chapel</title>
<link rel="stylesheet" href="https://fonts.googleapis.com/css2?family=Cinzel:wght@600;700&family=Crimson+Pro:wght@400&display=swap">
<style>
  :root {
    --orange: #f39a2b;
    --orange-deep: #e07b16;
    --blue: #1f8fd6;
    --blue-deep: #1166b0;
    --purple: #a33594;
    --purple-deep: #7d1f73;
    --ink: #3b3b3d;
    --ink-dark: #231f20;
    --disc: #f0f1f2;
    --track: #e4e5e7;
    --track-inner: #d8dadc;
    --ring: #b9bdc0;
    --node: #ffffff;
    --page: #ffffff;
  }
  html, body {
    margin: 0;
    padding: 0;
    width: 1200px;
    height: 1200px;
    overflow: hidden;
    background: var(--page);
  }
  .canvas {
    display: block;
    width: 1200px;
    height: 1200px;
  }
  .direction-label {
    font-family: "Cinzel", serif;
    font-weight: 700;
    font-size: 33px;
    letter-spacing: 0.5px;
    fill: var(--ink);
    text-anchor: middle;
  }
  .church-name {
    font-family: "Crimson Pro", serif;
    font-weight: 400;
    font-size: 42px;
    fill: var(--ink-dark);
    text-anchor: middle;
  }
  .icon-orange { fill: var(--orange); }
  .icon-blue { fill: var(--blue-deep); }
  .icon-purple { fill: var(--purple); }
</style>
</head>
<body>
<svg class="canvas" viewBox="0 0 1200 1200" xmlns="http://www.w3.org/2000/svg">
  <defs>
    <linearGradient id="ring-orange" x1="0" y1="0" x2="0" y2="1">
      <stop offset="0" stop-color="var(--orange)"/>
      <stop offset="1" stop-color="var(--orange-deep)"/>
    </linearGradient>
    <linearGradient id="ring-blue" x1="0" y1="0" x2="0" y2="1">
      <stop offset="0" stop-color="var(--blue)"/>
      <stop offset="1" stop-color="var(--blue-deep)"/>
    </linearGradient>
    <linearGradient id="ring-purple" x1="0" y1="0" x2="0" y2="1">
      <stop offset="0" stop-color="var(--purple)"/>
      <stop offset="1" stop-color="var(--purple-deep)"/>
    </linearGradient>
    <linearGradient id="ring-grey" x1="0" y1="0" x2="0" y2="1">
      <stop offset="0" stop-color="#d3d6d8"/>
      <stop offset="1" stop-color="#9fa3a6"/>
    </linearGradient>
    <radialGradient id="person-area" cx="0.5" cy="0.45" r="0.6">
      <stop offset="0" stop-color="#9a9c9e"/>
      <stop offset="1" stop-color="#e6e8e9"/>
    </radialGradient>
  </defs>

  <g class="gauge">
    <path class="gauge-track" d="M336 654 A264 264 0 0 1 864 654 Z" fill="var(--track)"/>
    <path class="band band-in" d="M356 654 A244 244 0 0 1 485.4 438.6 L513.6 491.5 A184 184 0 0 0 416 654 Z" fill="var(--orange)"/>
    <path class="band band-up" d="M485.4 438.6 A244 244 0 0 1 714.6 438.6 L686.4 491.5 A184 184 0 0 0 513.6 491.5 Z" fill="var(--blue-deep)"/>
    <path class="band band-out" d="M714.6 438.6 A244 244 0 0 1 844 654 L784 654 A184 184 0 0 0 686.4 491.5 Z" fill="var(--purple)"/>
    <path class="gauge-inner" d="M416 654 A184 184 0 0 1 784 654 Z" fill="var(--track-inner)"/>
    <rect class="gauge-base" x="290" y="654" width="620" height="8" rx="4" fill="var(--track)"/>
  </g>

  <g class="connectors">
    <line x1="292" y1="488" x2="415" y2="547" stroke="var(--orange)" stroke-width="12" stroke-linecap="round"/>
    <rect x="589" y="318" width="22" height="124" fill="var(--blue-deep)"/>
    <line x1="890" y1="488" x2="785" y2="547" stroke="var(--purple)" stroke-width="12" stroke-linecap="round"/>
  </g>

  <g class="nodes">
    <circle cx="415" cy="547" r="17" fill="var(--node)" stroke="var(--ring)" stroke-width="6"/>
    <circle cx="600" cy="440" r="17" fill="var(--node)" stroke="var(--ring)" stroke-width="6"/>
    <circle cx="785" cy="547" r="17" fill="var(--node)" stroke="var(--ring)" stroke-width="6"/>
  </g>

  <g class="person">
    <circle cx="600" cy="654" r="152" fill="url(#ring-grey)"/>
    <circle cx="600" cy="654" r="126" fill="var(--disc)"/>
    <circle cx="600" cy="654" r="112" fill="url(#person-area)" role="img" aria-label="Silhouette of a person at the centre of the three connections"/>
  </g>

  <g class="direction direction-in">
    <circle cx="194" cy="412" r="132" fill="url(#ring-orange)"/>
    <circle cx="194" cy="412" r="110" fill="var(--disc)"/>
    <g class="icon-orange" transform="translate(194 350)">
      <path d="M-20 -2 L0 -20 L20 -2 L15 -2 L15 16 L5 16 L5 4 L-5 4 L-5 16 L-15 16 L-15 -2 Z"/>
    </g>
    <text class="direction-label" x="194" y="404">In to</text>
    <text class="direction-label" x="194" y="438">the</text>
    <text class="direction-label" x="194" y="472">Church</text>
  </g>

  <g class="direction direction-up">
    <circle cx="598" cy="190" r="136" fill="url(#ring-blue)"/>
    <circle cx="598" cy="190" r="112" fill="var(--disc)"/>
    <g class="icon-blue" transform="translate(598 132)">
      <rect x="-4" y="-24" width="8" height="48"/>
      <rect x="-15" y="-12" width="30" height="7"/>
    </g>
    <text class="direction-label" x="598" y="200">Up to</text>
    <text class="direction-label" x="598" y="236">God</text>
  </g>

  <g class="direction direction-out">
    <circle cx="988" cy="410" r="136" fill="url(#ring-purple)"/>
    <circle cx="988" cy="410" r="112" fill="var(--disc)"/>
    <g class="icon-purple" transform="translate(988 340)">
      <circle r="15"/>
      <path d="M-15 0 H15 M0 -15 V15 M-11 -8 H11 M-11 8 H11" stroke="var(--disc)" stroke-width="2.5" fill="none"/>
      <ellipse rx="7" ry="15" fill="none" stroke="var(--disc)" stroke-width="2.5"/>
    </g>
    <text class="direction-label" x="988" y="388">Out</text>
    <text class="direction-label" x="988" y="422">to</text>
    <text class="direction-label" x="988" y="456">the</text>
    <text class="direction-label" x="988" y="490">World</text>
  </g>

  <g class="church-mark">
    <circle cx="600" cy="962" r="88" fill="var(--purple)"/>
    <text class="church-name" x="600" y="1106">Lakerow Family Chapel</text>
  </g>
</svg>
</body>
</html>
```